Garlic Farm for Farm Sales/Restaurant sales

Need a professional, but appealing to agriculture world. We are selling 27 kinds of Organic Garlic from a farm in Simla,CO. I have uploaded logo and business information-we are going to need a template, because I will need to use it for four separate people.
-We are trying to appeal to Farm to table restaurants
-As well as growers/farmers

Target Market(s)

Agriculture Sales/Restaurants-Organic

Industry/Entity Type

Agriculture

Contact Information for Business Card

Want it to look more unique then your average brimly ink card- I want it to look amazing

Font styles to use
Sans Serif

Colors
0455a3
ec1f27
fbed22
ffffff

Requirements
Must have
• Just be creative
Nice to have
• Colorful
Should not have
• plain

```html
<!DOCTYPE html>
<html lang="en">
<head>
<meta charset="utf-8">
<title>Plains Crest Garlic – Business Card</title>
<link rel="stylesheet" href="https://fonts.googleapis.com/css2?family=Mulish:wght@400;700&display=swap">
<style>
  :root {
    --navy: #0b2d5e;
    --crimson: #a8182f;
    --coral: #d4533f;
    --cream: #fcfad8;
    --icon-red: #d04a3a;
    --backdrop: #e9e7e2;
  }
  html, body {
    margin: 0;
    padding: 0;
    width: 1113px;
    height: 1200px;
    overflow: hidden;
    background: var(--backdrop);
  }
  .canvas {
    position: relative;
    width: 1113px;
    height: 1200px;
    font-family: "Mulish", sans-serif;
  }
  .card {
    position: absolute;
    width: 772px;
    height: 460px;
    filter: drop-shadow(0 2px 4px rgba(0,0,0,0.18));
  }
  .card--front { left: 178px; top: 128px; }
  .card--back  { left: 172px; top: 652px; }
  .card svg { display: block; width: 772px; height: 460px; }
  .brand-name { font-family: "Mulish", sans-serif; font-weight: 700; fill: var(--navy); }
  .person-name { font-family: "Mulish", sans-serif; font-weight: 700; fill: var(--navy); font-size: 25px; }
  .person-role { font-family: "Mulish", sans-serif; font-weight: 400; fill: var(--navy); font-size: 23px; }
  .contact-line { font-family: "Mulish", sans-serif; font-weight: 400; fill: var(--navy); font-size: 20px; }
  .icon { fill: none; stroke: var(--icon-red); stroke-width: 2; stroke-linecap: round; stroke-linejoin: round; }
  .icon-solid { fill: var(--icon-red); }
</style>
</head>
<body>
<main class="canvas">

  <!-- Front of card -->
  <section class="card card--front" aria-label="Card front">
    <svg viewBox="0 0 772 460" xmlns="http://www.w3.org/2000/svg">
      <defs>
        <clipPath id="front-shape">
          <path d="M0 0 H682 A90 90 0 0 1 772 90 V460 H90 A90 90 0 0 1 0 370 Z"/>
        </clipPath>
      </defs>
      <g clip-path="url(#front-shape)">
        <rect width="772" height="460" fill="var(--navy)"/>
        <circle cx="582" cy="262" r="440" fill="var(--coral)"/>
        <circle cx="578" cy="258" r="428" fill="var(--crimson)"/>
        <circle cx="582" cy="250" r="412" fill="var(--cream)"/>
      </g>
      <circle class="brand-mark" cx="448" cy="176" r="48" fill="var(--crimson)"/>
      <text class="brand-name" x="460" y="290" font-size="52" text-anchor="middle">plains crest</text>
      <text class="brand-name" x="460" y="330" font-size="26" text-anchor="middle">garlic</text>
    </svg>
  </section>

  <!-- Back of card -->
  <section class="card card--back" aria-label="Card back">
    <svg viewBox="0 0 772 460" xmlns="http://www.w3.org/2000/svg">
      <defs>
        <clipPath id="back-shape">
          <path d="M90 0 H772 V370 A90 90 0 0 1 682 460 H0 V90 A90 90 0 0 1 90 0 Z"/>
        </clipPath>
      </defs>
      <g clip-path="url(#back-shape)">
        <rect width="772" height="460" fill="var(--navy)"/>
        <circle cx="206" cy="226" r="448" fill="var(--coral)"/>
        <circle cx="210" cy="230" r="436" fill="var(--crimson)"/>
        <circle cx="196" cy="232" r="424" fill="var(--cream)"/>
      </g>

      <circle class="brand-mark" cx="497" cy="72" r="30" fill="var(--crimson)"/>
      <text class="brand-name" x="500" y="136" font-size="30" text-anchor="middle">plains crest</text>
      <text class="brand-name" x="500" y="158" font-size="16" text-anchor="middle">garlic</text>

      <text class="person-name" x="64" y="170">Your Name</text>
      <text class="person-role" x="64" y="202">Position</text>

      <!-- phone -->
      <path class="icon" d="M68 228 q2 -4 6 -2 l3 5 q1 2 -1 4 l-2 1 q2 5 7 8 l1 -2 q2 -2 4 -1 l4 3 q2 3 -2 6 q-6 2 -14 -7 q-8 -9 -6 -15 z"/>
      <text class="contact-line" x="112" y="240">123-456-7890</text>

      <!-- mobile -->
      <rect class="icon" x="69" y="257" width="12" height="20" rx="2"/>
      <line class="icon" x1="73" y1="273" x2="77" y2="273"/>
      <text class="contact-line" x="112" y="275">123-456-7888</text>

      <!-- mail -->
      <rect class="icon" x="66" y="296" width="19" height="13" rx="1"/>
      <path class="icon" d="M66 297 l9.5 7 l9.5 -7"/>
      <text class="contact-line" x="112" y="310">name@companyname.com</text>

      <!-- globe -->
      <circle class="icon" cx="75.5" cy="338" r="9.5"/>
      <ellipse class="icon" cx="75.5" cy="338" rx="4" ry="9.5"/>
      <line class="icon" x1="66" y1="338" x2="85" y2="338"/>
      <text class="contact-line" x="112" y="345">www.companyname.com</text>

      <!-- pin -->
      <path class="icon-solid" d="M75.5 386 c-5 -7 -9 -11 -9 -16 a9 9 0 0 1 18 0 c0 5 -4 9 -9 16 z"/>
      <circle cx="75.5" cy="370" r="3.2" fill="var(--cream)"/>
      <text class="contact-line" x="112" y="380">address</text>
    </svg>
  </section>

</main>
</body>
</html>
```